Business Card Design for a Personal Trainer

I need a business card design for my job as a personal trainer. It should have a unique, modern and exclusive design. On the front there should be only my logo with my name and my job. 0163/2918374 Tobias Kellinger Lindenfeldweg 14 80412 Munich Germany The most important contact information is the web adress. it can be bigger than the rest, but its not necessary. The card should be 8,5cmx5,5cm big. Font: Roboto. Colors: black, white, gray, 56c1ff.

```html
<!DOCTYPE html>
<html lang="de">
<head>
<meta charset="utf-8">
<title>Tobias Kellinger – Personal Trainer Visitenkarte</title>
<link href="https://fonts.googleapis.com/css2?family=Roboto:wght@400;500&display=swap" rel="stylesheet">
<style>
  :root {
    --backdrop: #e9e9e9;
    --card: #262626;
    --emboss: #3c3c3c;
    --white: #ffffff;
    --accent: #56c1ff;
    --photo-light: #6a6a6a;
    --photo-dark: #2a2a2a;
  }
  * { margin: 0; padding: 0; box-sizing: border-box; }
  html, body {
    width: 1200px; height: 1000px; overflow: hidden;
    background: var(--backdrop);
    font-family: "Roboto", Arial, sans-serif;
  }
  .card {
    position: absolute; left: 232px;
    width: 736px; height: 418px;
    background: var(--card);
    color: var(--white);
  }
  .card--front { top: 55px; }
  .card--back { top: 531px; }

  /* Front */
  .front-name {
    position: absolute; left: 0; right: 0; top: 218px;
    text-align: center; font-size: 44px; font-weight: 400;
    color: var(--emboss); letter-spacing: 1px;
  }
  .front-title {
    position: absolute; left: 0; right: 0; top: 266px;
    text-align: center; font-size: 18px; letter-spacing: 4px;
    color: var(--emboss);
  }
  .front-web {
    position: absolute; left: 0; right: 0; top: 358px;
    text-align: center; font-size: 19px; letter-spacing: 1px;
  }
  .accent { color: var(--accent); }

  /* Back */
  .brand {
    position: absolute; left: 39px; top: 64px;
    display: flex; align-items: center; gap: 12px;
  }
  .brand-square { width: 22px; height: 22px; background: var(--accent); }
  .brand-name { font-size: 24px; font-weight: 500; color: var(--accent); letter-spacing: 2px; }

  .name-bar {
    position: absolute; left: 0; top: 169px;
    width: 8px; height: 48px; background: var(--accent);
  }
  .contact { position: absolute; left: 39px; top: 163px; }
  .contact-name { font-size: 27px; font-weight: 500; color: var(--accent); line-height: 32px; }
  .contact-title { font-size: 20px; line-height: 28px; }
  .contact-address { margin-top: 14px; font-size: 20px; line-height: 27px; }
  .contact-list { list-style: none; margin-top: 14px; }
  .contact-list li {
    display: flex; align-items: center; gap: 8px;
    font-size: 20px; line-height: 27px;
  }
  .contact-list svg { width: 15px; height: 15px; fill: var(--accent); }

  .portrait {
    position: absolute; left: 463px; top: 20px;
    width: 255px; height: 398px;
    background: radial-gradient(ellipse at 50% 35%, var(--photo-light), var(--photo-dark) 70%, var(--card));
  }
</style>
</head>
<body>
  <section class="card card--front">
    <div class="front-name">TOBIAS KELLINGER</div>
    <div class="front-title">PERSONAL TRAINER</div>
    <div class="front-web">www.<span class="accent">tobiaskellinger</span>.de</div>
  </section>

  <section class="card card--back">
    <div class="brand">
      <span class="brand-square"></span>
      <span class="brand-name">TOBIAS KELLINGER</span>
    </div>

    <div class="name-bar"></div>
    <div class="contact">
      <div class="contact-name">Tobias Kellinger</div>
      <div class="contact-title">Personal Trainer</div>
      <div class="contact-address">Lindenfeldweg 14<br>80412 München</div>
      <ul class="contact-list">
        <li>
          <svg viewBox="0 0 24 24"><path d="M6.6 10.8a15.1 15.1 0 0 0 6.6 6.6l2.2-2.2a1 1 0 0 1 1-.25 11.4 11.4 0 0 0 3.6.57 1 1 0 0 1 1 1V20a1 1 0 0 1-1 1A17 17 0 0 1 3 4a1 1 0 0 1 1-1h3.5a1 1 0 0 1 1 1c0 1.25.2 2.45.57 3.57a1 1 0 0 1-.25 1z"/></svg>
          0163/2918374
        </li>
        <li>
          <svg viewBox="0 0 24 24"><path d="M2 5h20v14H2z M2 5l10 8 10-8" /><path d="M3 6.5l9 7 9-7V18H3z" fill="#262626" opacity="0"/></svg>
          t.kellinger@mailpost.de
        </li>
        <li>
          <svg viewBox="0 0 24 24"><circle cx="12" cy="12" r="10"/><path d="M2 12h20M12 2c3 3 3 17 0 20M12 2c-3 3-3 17 0 20" stroke="#262626" stroke-width="1.5" fill="none"/></svg>
          www.<span class="accent">tobiaskellinger</span>.de
        </li>
      </ul>
    </div>

    <div class="portrait" role="img" aria-label="Schwarz-weißes Porträtfoto des Personal Trainers mit verschränkten Armen"></div>
  </section>
</body>
</html>
```